Startup Technology Consulting Firm in NYC Needs A Website

I need a website built for my startup technology consulting company Brightmoor Systems Collective. We offer a unique white glove service that provides end to end technology support. I want to stand out above the rest. We are small firm but are very dedicated which where we derive our name from BSC primarily offers
end to end technology advisory services to small businesses lacking their own IT staff. We offer top notch white glove and our customer service and satisfaction is exceed by no one.

Below are some of what we provide our clients

Strategic IT Planning
Business Continuity Planning/Disaster Recovery
Cloud Computing\DataCenter Solutions
Server Infrastructure/Networking
Virtualization Technologies
Project Management

Our Technology Advisors hold many certifications from Quillora & Tessfold. We are also Quillora Partners

I have attached my logo (preview design) As soon as I ge the final images I will upload.

Reason: want to give more time to submit designs

Industry/Entity Type

Information Technology

Coding

Coded - Design and coding required

Number of Pages Required

1 page

Font styles to use
Sans Serif

Requirements
Must have
• Attract Target Market. The site should bleed the company vision
• DEDICATION everything about the site should show this
• Layout the Benefits of our offerings
• Links to my social media
• Links to dircct my client's for remote support

```html
<!DOCTYPE html>
<html lang="en">
<head>
<meta charset="utf-8">
<title>Brightmoor Systems Collective</title>
<link rel="stylesheet" href="https://fonts.googleapis.com/css2?family=Open+Sans:wght@400;600&family=Ubuntu:wght@400;500;700&display=swap">
<style>
:root{
  --blue:#1b84c6;
  --blue-dark:#1a6aa8;
  --ink:#333;
  --muted:#8a8a8a;
  --line:#e6e6e6;
  --band:#f4f4f4;
  --footer:#1d7ec2;
}
*{margin:0;padding:0;box-sizing:border-box}
html,body{width:673px;height:1200px;overflow:hidden;background:#fff}
body{position:relative;font-family:"Open Sans",sans-serif;color:var(--ink)}
.abs{position:absolute}
.head{font-family:"Ubuntu",sans-serif}

/* header */
.topbar{left:0;top:0;width:673px;height:2px;background:var(--blue)}
.brand{left:55px;top:18px;display:flex;align-items:center;gap:6px}
.brand-dot{width:22px;height:22px;border-radius:50%;background:var(--blue-dark)}
.brand-name{font-family:"Ubuntu",sans-serif;font-weight:500;font-size:10px;line-height:12px;color:var(--blue-dark);width:96px}
.nav{top:30px;font-size:7.5px;color:#444;letter-spacing:.2px}
.nav-active{left:351px;top:63px;width:22px;height:2px;background:var(--blue)}

/* hero */
.hero{left:0;top:66px;width:673px;height:301px;background:linear-gradient(90deg,#0c1622 0%,#16263a 45%,#0e2a4c 70%,#0a1626 100%)}
.hero-kicker{left:396px;top:196px;color:#fff;font-weight:700;font-size:15.5px}
.hero-title{left:396px;top:213px;color:#fff;font-weight:700;font-size:33px;letter-spacing:.5px}
.hero-arrow{top:203px;width:20px;height:20px;border-radius:50%;background:rgba(255,255,255,.12)}

/* services */
.section-title{left:0;width:673px;text-align:center;font-size:17px}
.section-title span{color:var(--blue)}
.intro{left:120px;top:421px;width:433px;text-align:center;font-size:6px;line-height:11.5px;color:#555}
.svc{width:190px;height:40px}
.svc-icon{left:0;top:0;width:36px;height:36px;border-radius:50%;border:1px solid #bbb;display:flex;align-items:center;justify-content:center}
.svc-icon.on{background:var(--blue);border-color:var(--blue)}
.svc-name{left:47px;top:3px;font-size:8.5px;color:#555;white-space:nowrap}
.svc-text{left:47px;top:18px;font-size:6px;line-height:10.5px;color:var(--muted);width:140px}

/* testimonial */
.quotes{left:0;top:627px;width:673px;height:196px;background:linear-gradient(180deg,#1b2430 0%,#2a3646 40%,#1b222c 100%)}
.quote-text{left:118px;top:701px;width:437px;text-align:center;font-size:6.5px;line-height:12.5px;color:#eee}
.qmark{font-family:Georgia,serif;font-style:italic;font-weight:700;font-size:14px;color:#fff}
.dot{top:778px;width:9px;height:9px;border-radius:50%;border:1px solid #ddd}

/* welcome + blog */
.block-title{top:851px;font-size:11.5px;color:#333}
.photo{background:linear-gradient(135deg,#8a7f78,#c9ccd3 45%,#e6eaee)}
.post-title{font-size:7.5px;color:#444}
.post-date{font-size:6px;color:var(--blue);font-weight:600}
.post-text{font-size:6px;line-height:11.5px;color:#666}

/* contact */
.contact{left:0;top:1070px;width:673px;height:76px;background:var(--band)}
.contact-text{font-size:7px;line-height:13.5px;color:#444}
.partner{font-family:"Ubuntu",sans-serif;font-size:15px;font-weight:500;color:#666;display:flex;align-items:center;gap:5px}
.partner i{display:block;width:14px;height:14px;background:#888}

/* footer */
.footer{left:0;top:1146px;width:673px;height:54px;background:var(--footer)}
.social{top:1159px;width:14px;height:14px;border-radius:50%;border:1px solid #dfefff}
.copyright{left:0;top:1180px;width:673px;text-align:center;font-size:6.5px;color:#e6f2fb}
</style>
</head>
<body>

<header>
  <div class="abs topbar"></div>
  <div class="abs brand"><span class="brand-dot"></span><span class="brand-name">Brightmoor Systems Collective</span></div>
  <nav>
    <span class="abs nav" style="left:352px">HOME</span>
    <span class="abs nav" style="left:398px">ABOUT US</span>
    <span class="abs nav" style="left:456px">OUR SERVICES</span>
    <span class="abs nav" style="left:530px">BLOG</span>
    <span class="abs nav" style="left:573px">CONTACT US</span>
  </nav>
  <div class="abs nav-active"></div>
</header>

<section>
  <div class="abs hero" role="img" aria-label="Consultant in a suit using a tablet in front of a glowing server room"></div>
  <div class="abs head hero-kicker">SERVER INFRASTRUCTURE</div>
  <div class="abs head hero-title">NETWORKING</div>
  <svg class="abs hero-arrow" style="left:30px" viewBox="0 0 20 20"><path d="M11.5 6 7.5 10l4 4" fill="none" stroke="#ccc" stroke-width="1.4"/></svg>
  <svg class="abs hero-arrow" style="left:627px" viewBox="0 0 20 20"><path d="M8.5 6l4 4-4 4" fill="none" stroke="#ccc" stroke-width="1.4"/></svg>
</section>

<section>
  <h2 class="abs head section-title" style="top:394px;font-weight:400">OUR <span>SERVICES</span></h2>
  <p class="abs intro">Lorem ipsum dolor sit amet, consectetur adipiscing elit, sed do eiusmod tempor incididunt ut labore et dolore magna aliqua. Ut enim ad minim veniam, quis nostrud exercitation ullamco laboris nisi ut aliquip ex ea commodo consequat. Duis aute irure</p>

  <div class="abs svc" style="left:55px;top:494px">
    <div class="abs svc-icon on"><svg width="14" height="14" viewBox="0 0 14 14"><circle cx="7" cy="5.5" r="3.5" fill="none" stroke="#fff" stroke-width="1.2"/><path d="M5.5 9.5h3M5.8 11.5h2.4" stroke="#fff" stroke-width="1.2"/></svg></div>
    <div class="abs head svc-name">Strategic IT Planning</div>
    <div class="abs svc-text">Lorem ipsum dolor sit amet, consectetur adipiscing elit, sed do eiusmod</div>
  </div>
  <div class="abs svc" style="left:254px;top:494px">
    <div class="abs svc-icon"><svg width="14" height="14" viewBox="0 0 14 14"><path d="M2 4h3a2 2 0 1 1 4 0h3v8H2z" fill="#666"/></svg></div>
    <div class="abs head svc-name">Business Continuity Planning</div>
    <div class="abs svc-text">Lorem ipsum dolor sit amet, consectetur adipiscing elit, sed do eiusmod</div>
  </div>
  <div class="abs svc" style="left:451px;top:494px">
    <div class="abs svc-icon"><svg width="16" height="12" viewBox="0 0 16 12"><path d="M4 11a3 3 0 0 1 0-6 4.5 4.5 0 0 1 8.5-1A3.5 3.5 0 0 1 12 11z" fill="#666"/></svg></div>
    <div class="abs head svc-name">Cloud Computing</div>
    <div class="abs svc-text">Lorem ipsum dolor sit amet, consectetur adipiscing elit, sed do eiusmod</div>
  </div>
  <div class="abs svc" style="left:55px;top:560px">
    <div class="abs svc-icon"><svg width="12" height="14" viewBox="0 0 12 14"><ellipse cx="6" cy="2.5" rx="5.5" ry="2" fill="#666"/><path d="M.5 4.5q5.5 3 11 0v2q-5.5 3-11 0zM.5 8.5q5.5 3 11 0v2q-5.5 3-11 0z" fill="#666"/></svg></div>
    <div class="abs head svc-name">Server Infrastructure</div>
    <div class="abs svc-text">Lorem ipsum dolor sit amet, consectetur adipiscing elit, sed do eiusmod</div>
  </div>
  <div class="abs svc" style="left:254px;top:560px">
    <div class="abs svc-icon"><svg width="15" height="13" viewBox="0 0 15 13"><ellipse cx="6" cy="5" rx="5.5" ry="4" fill="#666"/><ellipse cx="10" cy="8" rx="4.5" ry="3.3" fill="#666"/></svg></div>
    <div class="abs head svc-name">Virtualisation Technologies</div>
    <div class="abs svc-text">Lorem ipsum dolor sit amet, consectetur adipiscing elit, sed do eiusmod</div>
  </div>
  <div class="abs svc" style="left:451px;top:560px">
    <div class="abs svc-icon"><svg width="15" height="13" viewBox="0 0 15 13"><rect x="1" y="1" width="13" height="8.5" fill="none" stroke="#666" stroke-width="1.5"/><path d="M5 12h5M7.5 9.5V12" stroke="#666" stroke-width="1.5"/></svg></div>
    <div class="abs head svc-name">Project Management</div>
    <div class="abs svc-text">Lorem ipsum dolor sit amet, consectetur adipiscing elit, sed do eiusmod</div>
  </div>
</section>

<section>
  <div class="abs quotes" role="img" aria-label="City skyline at dusk under a cloudy sky"></div>
  <h2 class="abs head section-title" style="top:666px;color:#fff;font-weight:400">WHAT OUR CLIENTS SAY</h2>
  <span class="abs qmark" style="left:98px;top:696px">&ldquo;</span>
  <p class="abs quote-text">Lorem ipsum dolor sit amet, consectetur adipiscing elit, sed do eiusmod tempor incididunt ut labore et dolore magna aliqua. Ut enim ad minim veniam, quis nostrud exercitation ullamco laboris nisi ut aliquip ex ea commodo consequat. Duis aute irure dolor in reprehenderit in voluptate velit esse cillum dolore eu fugiat nulla pariatur. Excepteur sint occaecat cupidatat non</p>
  <span class="abs qmark" style="left:568px;top:721px">&rdquo;</span>
  <div class="abs" style="left:0;top:752px;width:673px;text-align:center;font-size:7.5px;color:#fff">MARA ELLISON</div>
  <span class="abs dot" style="left:316px;background:var(--blue);border-color:var(--blue);width:10px;height:10px;top:777px"></span>
  <span class="abs dot" style="left:334px"></span>
  <span class="abs dot" style="left:349px"></span>
</section>

<section>
  <h3 class="abs head block-title" style="left:55px;font-weight:400">WELCOME TO BSC</h3>
  <div class="abs photo" style="left:55px;top:877px;width:203px;height:107px" role="img" aria-label="Hand holding a magnifying glass beside a glowing globe"></div>
  <div class="abs post-title" style="left:55px;top:995px">Nemo enim ipsam voluptatem</div>
  <p class="abs post-text" style="left:55px;top:1010px;width:210px">Lorem ipsum dolor sit amet, consectetur adipiscing elit, sed do eiusmod tempor incididunt ut labore et dolore magna aliqua. Ut enim ad minim veniam, quis nostrud exercitation</p>

  <h3 class="abs head block-title" style="left:318px;font-weight:400">LATEST BLOG</h3>
  <div class="abs photo" style="left:318px;top:878px;width:77px;height:65px;background:linear-gradient(135deg,#3b4f6e,#9fb4cc)" role="img" aria-label="Two colleagues reviewing documents at a desk"></div>
  <div class="abs post-title" style="left:409px;top:878px">Nemo Enim Ipsam Voluptatem</div>
  <div class="abs post-date" style="left:409px;top:895px">JULY 10, 2015</div>
  <p class="abs post-text" style="left:409px;top:908px;width:205px">Lorem ipsum dolor sit amet, consectetur adipiscing elit, sed do eiusmod tempor incididunt ut labore et dolore magna aliqua. Ut enim ad minim veniam, quis nostrud</p>
  <div class="abs" style="left:318px;top:959px;width:300px;height:1px;background:var(--line)"></div>
  <div class="abs photo" style="left:318px;top:976px;width:77px;height:64px;background:linear-gradient(135deg,#18232f,#2f4a66 60%,#8fb0cc)" role="img" aria-label="Person touching a glowing digital globe interface"></div>
  <div class="abs post-title" style="left:409px;top:974px">Nemo Enim Ipsam Voluptatem</div>
  <div class="abs post-date" style="left:409px;top:991px">JULY 10, 2015</div>
  <p class="abs post-text" style="left:409px;top:1004px;width:205px">Lorem ipsum dolor sit amet, consectetur adipiscing elit, sed do eiusmod tempor incididunt ut labore et dolore magna aliqua. Ut enim ad minim veniam, quis nostrud</p>
</section>

<section>
  <div class="abs contact"></div>
  <div class="abs" style="left:54px;top:1087px;font-size:8.5px;color:#333">CONTACT US</div>
  <svg class="abs" style="left:54px;top:1104px" width="10" height="14" viewBox="0 0 10 14"><path d="M5 13.5C2 9 .5 6.8.5 5a4.5 4.5 0 0 1 9 0c0 1.8-1.5 4-4.5 8.5z" fill="#999"/><circle cx="5" cy="5" r="1.7" fill="var(--band)"/></svg>
  <div class="abs contact-text" style="left:74px;top:1103px">418 Linden Row,<br>Harrow Falls 20418, USA.</div>
  <svg class="abs" style="left:207px;top:1105px" width="10" height="10" viewBox="0 0 10 10"><path d="M2 1l2 2-1 1.5q1 2 2.5 2.5L7 6l2 2-1.5 1.5Q3 9 .5 2.5z" fill="none" stroke="#999" stroke-width=".9"/></svg>
  <div class="abs" style="left:226px;top:1103px;font-size:8.5px;color:#444">+1 555-014-2290</div>
  <svg class="abs" style="left:207px;top:1121px" width="11" height="8" viewBox="0 0 11 8"><rect x=".5" y=".5" width="10" height="7" fill="none" stroke="#999"/><path d="M.5.5 5.5 4.5l5-4" fill="none" stroke="#999"/></svg>
  <div class="abs contact-text" style="left:226px;top:1118px">info@bsc-advisory.example</div>
  <div class="abs partner" style="left:366px;top:1104px"><i></i>Quillora</div>
  <div class="abs partner" style="left:491px;top:1104px"><i style="background:none;border:1.5px solid #888"></i>Tessfold</div>
</section>

<footer>
  <div class="abs footer"></div>
  <span class="abs social" style="left:296px" aria-label="Social link"></span>
  <span class="abs social" style="left:313px" aria-label="Social link"></span>
  <span class="abs social" style="left:330px" aria-label="Social link"></span>
  <span class="abs social" style="left:347px" aria-label="Social link"></span>
  <span class="abs social" style="left:364px" aria-label="Social link"></span>
  <div class="abs copyright">©2014 - 2015 &nbsp;BSC., All Rights Reserved.</div>
</footer>

</body>
</html>
```